Business Card Design for Flood Rescue 360 - Property Restoration Professionals

I need a business card designed for Flood Rescue 360. We are a full-service property restoration solution. Providing water, fire, smoke & storm restoration as well as mold remediation and full remodel or reconstruction to homes and businesses across Dallas-Fort Worth, TX.
Target Market(s)
home and business owners with insurance covered property damage from water, fire or storm related damage
Industry/Entity Type
property restoration
Contact Information for Business Card
Martin Kell General Manager Cell: 214-555-0193 Office: 469-555-0148 email: Martin@FloodRescue360.example services: Water, Fire, Mold, Reconstruction Tagline: Urgency for Your Water Emergency!
Look and feel
Each slider illustrates characteristics of the customer's brand and the style your logo design should communicate.

```html
<!DOCTYPE html>
<html lang="en">
<head>
<meta charset="utf-8">
<title>Flood Rescue 360 – Business Card</title>
<link rel="stylesheet" href="https://fonts.googleapis.com/css2?family=Poppins:wght@400&family=Open+Sans:wght@400;600&display=swap">
<style>
  :root {
    --brand-blue: #00b2e6;
    --ink-grey: #58595b;
    --soft-grey: #f3f3f3;
    --paper: #ffffff;
    --stage: #262626;
  }
  * { box-sizing: border-box; margin: 0; padding: 0; }
  html, body { width: 1200px; height: 952px; overflow: hidden; }
  body {
    background: var(--stage);
    display: flex; align-items: center; justify-content: center; gap: 40px;
    font-family: "Open Sans", sans-serif;
  }
  .card {
    position: relative; width: 540px; height: 309px; overflow: hidden;
    box-shadow: 0 10px 30px rgba(0,0,0,.5);
  }

  /* Front */
  .card-front { background: var(--paper); }
  .company-name {
    font-family: "Open Sans", sans-serif; font-weight: 600;
    color: var(--brand-blue); white-space: nowrap;
  }
  .card-front .company-name {
    position: absolute; left: 34px; top: 34px; font-size: 26px; line-height: 1.2;
  }
  .person { position: absolute; left: 34px; top: 110px; }
  .person-name {
    font-family: "Open Sans", sans-serif; font-weight: 600; text-transform: uppercase;
    color: var(--brand-blue); font-size: 19px; letter-spacing: .5px;
  }
  .person-title { color: var(--ink-grey); font-size: 12px; margin-top: -2px; }
  .rule { width: 36px; height: 1px; background: var(--ink-grey); margin: 7px 0 8px; }
  .contact-list { list-style: none; }
  .contact-list li {
    display: flex; align-items: center; gap: 7px; color: var(--ink-grey);
    font-size: 11.5px; line-height: 19px;
  }
  .contact-icon {
    width: 14px; height: 14px; background: var(--ink-grey); border-radius: 2px;
    display: flex; align-items: center; justify-content: center;
  }
  .tagline-band {
    position: absolute; left: 0; bottom: 44px; width: 310px; height: 32px;
    background: var(--brand-blue);
    clip-path: polygon(0 0, 100% 0, 93% 100%, 0 100%);
    color: var(--paper); font-size: 12px; font-weight: 600; text-transform: uppercase;
    display: flex; align-items: center; padding-left: 34px; letter-spacing: .2px;
  }

  /* Back */
  .card-back { background: var(--brand-blue); }
  .card-back .company-name {
    position: absolute; left: 0; right: 0; top: 82px; text-align: center;
    color: var(--paper); font-size: 40px; line-height: 1.2;
  }
  .service-band {
    position: absolute; left: 0; right: 0; bottom: 40px; height: 42px; background: var(--paper);
    display: flex; align-items: center; justify-content: center; gap: 18px;
    font-family: "Poppins", sans-serif; color: var(--ink-grey); font-size: 17px;
  }
  .service-band span::before { content: "•"; color: var(--brand-blue); margin-right: 5px; }
</style>
</head>
<body>
  <section class="card card-front">
    <p class="company-name">Flood Rescue 360</p>
    <div class="person">
      <h1 class="person-name">Martin Kell</h1>
      <p class="person-title">General Manager</p>
      <div class="rule"></div>
      <ul class="contact-list">
        <li><span class="contact-icon"><svg width="10" height="10" viewBox="0 0 24 24"><path fill="#fff" d="M6.6 10.8a15 15 0 0 0 6.6 6.6l2.2-2.2a1 1 0 0 1 1-.25 11.4 11.4 0 0 0 3.6.57 1 1 0 0 1 1 1V20a1 1 0 0 1-1 1A17 17 0 0 1 3 4a1 1 0 0 1 1-1h3.5a1 1 0 0 1 1 1c0 1.25.2 2.45.57 3.57a1 1 0 0 1-.25 1z"/></svg></span>214-555-0193</li>
        <li><span class="contact-icon"><svg width="10" height="10" viewBox="0 0 24 24"><rect x="3" y="8" width="18" height="12" rx="2" fill="#fff"/><path d="M6 8V5h12v3" stroke="#fff" stroke-width="2" fill="none"/></svg></span>469-555-0148</li>
        <li><span class="contact-icon"><svg width="10" height="10" viewBox="0 0 24 24"><rect x="2" y="5" width="20" height="14" fill="#fff"/><path d="M2 5l10 8 10-8" stroke="#58595b" stroke-width="2" fill="none"/></svg></span>Martin@FloodRescue360.example</li>
      </ul>
    </div>
    <div class="tagline-band">Urgency for your water emergency!</div>
  </section>

  <section class="card card-back">
    <p class="company-name">Flood Rescue 360</p>
    <div class="service-band">
      <span>Water</span><span>Fire</span><span>Mold</span><span>Reconstruction</span>
    </div>
  </section>
</body>
</html>
```